Kestrel Homes Australia Business Card

We need a Business Card design for our new start up company.
A unique model designed to address Australia’s growing housing affordability problem has been launched. More than half of Australians are being priced out of the property market and have resigned themselves to the fact that they may never be able to afford a home.
We have developed a unique Algorithm that allows people to get into property and reverse this trend of domination by the property investors in this country. The first of its kind model facilitates connecting people to lending facilities that do not require them to have the finance combined under the purchase contract.
Ownership is shared with a second-tier investor, made up of either family or friends if not, Kestrel Homes Australia will provide a mini property investor enabling thousands of people the opportunity to buy a home, which they otherwise thought was not possible.
Kestrel Homes Australia is addressing housing affordability for families and individuals, giving every Australian looking to buy a home the opportunity to enter the property market to live in or invest.
Under our unique model, there is no combined finance, and individuals are assessed for their percentage portion of the property only. “A unique feature of our product is it is based around the strategies used for property investment. I have developed a unique Algorithm that enables the Home buyer to purchase 60% of a property, while Kestrel Homes Australia facilitates a second-tier investor to buy the other 40%. The Algorithm locks the investor in place and enables the home buyer to stairway to full ownership. The investment is secured against real property.
Please refer to our website www.kestrelhomes.com.au for inspiration.
Also please find attached our logo.
Any further directions please ask.
Cheers Marcus
Industry/Entity Type
Real Estate
Contact Information for Business Card
Marcus Thorley
CEO
Mobile 0400 615 272
www.kestrelhomes.com.au
Email: marcus@kestrelhomes.com.au
Colors
Designer to choose colors to be used in the design.
Look and feel

```html
<!DOCTYPE html>
<html lang="en">
<head>
<meta charset="utf-8">
<title>Kestrel Homes Australia — Business Card</title>
<link rel="stylesheet" href="https://fonts.googleapis.com/css2?family=Open+Sans:wght@400;700&family=Montserrat:wght@500;600&display=swap">
<style>
  :root {
    --bg: #ecebe8;
    --card: #ffffff;
    --green: #34b04a;
    --green-dark: #4a8f3a;
    --blue: #07a9d3;
    --blue-text: #0ea6cf;
    --ink: #5b5b5b;
    --ink-soft: #666666;
  }
  * { margin: 0; padding: 0; box-sizing: border-box; }
  html, body { width: 1200px; height: 1000px; overflow: hidden; }
  body { background: var(--bg); position: relative; font-family: "Open Sans", Arial, sans-serif; }

  .card {
    position: absolute;
    width: 520px;
    height: 290px;
    background: var(--card);
    border-radius: 22px;
    overflow: hidden;
    box-shadow: 0 6px 18px rgba(0,0,0,0.18);
  }
  .card--front { left: 150px; top: 170px; }
  .card--back { left: 530px; top: 540px; }

  .card__art { position: absolute; inset: 0; width: 100%; height: 100%; }

  .brand-mark {
    position: absolute;
    left: 34px; top: 118px;
    width: 150px;
    font-family: "Montserrat", Arial, sans-serif;
    font-weight: 600;
    font-size: 18px;
    line-height: 1.2;
    color: var(--blue-text);
  }

  .contact {
    position: absolute;
    left: 215px; top: 92px;
    color: var(--ink);
  }
  .contact__name { font-weight: 700; font-size: 22px; line-height: 1.1; color: var(--ink); }
  .contact__role { font-size: 18px; margin-top: 2px; color: var(--ink-soft); }
  .contact__list { list-style: none; margin-top: 10px; }
  .contact__item { display: flex; align-items: center; gap: 10px; font-size: 14px; line-height: 22px; color: var(--ink-soft); }
  .contact__icon { width: 13px; height: 13px; fill: var(--ink); flex: none; }

  .back__logo {
    position: absolute;
    left: 0; right: 0; top: 96px;
    text-align: center;
  }
  .back__dot {
    display: block;
    width: 34px; height: 34px;
    margin: 0 auto 12px;
    border-radius: 50%;
    background: var(--blue);
  }
  .back__name {
    font-family: "Montserrat", Arial, sans-serif;
    font-weight: 600;
    font-size: 23px;
    color: var(--blue-text);
  }
  .back__tagline {
    font-family: "Montserrat", Arial, sans-serif;
    font-weight: 500;
    font-size: 12.5px;
    color: var(--green-dark);
    margin-top: 4px;
  }
</style>
</head>
<body>

  <section class="card card--front" aria-label="Business card front">
    <svg class="card__art" viewBox="0 0 520 290" aria-hidden="true">
      <path d="M0 0 H310 C190 15 70 60 0 150 Z" fill="var(--green)"/>
      <path d="M230 38 C320 18 410 30 470 68 C400 46 320 36 230 38 Z" fill="var(--green)"/>
      <path d="M520 120 C495 225 330 285 140 272 Q300 300 520 290 Z" fill="var(--blue)"/>
    </svg>

    <div class="brand-mark">Kestrel Homes Australia</div>

    <div class="contact">
      <p class="contact__name">Marcus Thorley</p>
      <p class="contact__role">CEO</p>
      <ul class="contact__list">
        <li class="contact__item">
          <svg class="contact__icon" viewBox="0 0 24 24"><path d="M6.6 10.8a15.1 15.1 0 0 0 6.6 6.6l2.2-2.2a1 1 0 0 1 1-.25 11.4 11.4 0 0 0 3.6.57 1 1 0 0 1 1 1V20a1 1 0 0 1-1 1A17 17 0 0 1 3 4a1 1 0 0 1 1-1h3.5a1 1 0 0 1 1 1c0 1.25.2 2.45.57 3.57a1 1 0 0 1-.25 1z"/></svg>
          0400 615 272
        </li>
        <li class="contact__item">
          <svg class="contact__icon" viewBox="0 0 24 24"><path d="M2 5h20v14H2zm2 2v.5l8 5 8-5V7zm0 2.8V17h16V9.8l-8 5z"/></svg>
          www.kestrelhomes.com.au
        </li>
        <li class="contact__item">
          <svg class="contact__icon" viewBox="0 0 24 24"><path d="M12 2a10 10 0 1 0 0 20 10 10 0 0 0 0-20zm6.9 6h-3a15.7 15.7 0 0 0-1.4-3.6A8 8 0 0 1 18.9 8zM12 4c.8 1.2 1.5 2.5 1.9 4h-3.8c.4-1.5 1.1-2.8 1.9-4zM4.3 14a8 8 0 0 1 0-4h3.4a16 16 0 0 0 0 4zm.8 2h3a15.7 15.7 0 0 0 1.4 3.6A8 8 0 0 1 5.1 16zm3-8h-3a8 8 0 0 1 4.3-3.6C8.9 5.5 8.4 6.7 8.1 8zM12 20c-.8-1.2-1.5-2.5-1.9-4h3.8c-.4 1.5-1.1 2.8-1.9 4zm2.3-6H9.7a14.7 14.7 0 0 1 0-4h4.6a14.7 14.7 0 0 1 0 4zm.3 5.6c.6-1.1 1.1-2.3 1.4-3.6h3a8 8 0 0 1-4.4 3.6zM16.3 14a16 16 0 0 0 0-4h3.4a8 8 0 0 1 0 4z"/></svg>
          marcus@kestrelhomes.com.au
        </li>
      </ul>
    </div>
  </section>

  <section class="card card--back" aria-label="Business card back">
    <div class="back__logo">
      <span class="back__dot"></span>
      <p class="back__name">Kestrel Homes Australia</p>
      <p class="back__tagline">Opening Doors to Owning a Home</p>
    </div>
  </section>

</body>
</html>
```